Business Card Design Project

We need a new fresh business card for our business. There are multiple services we offer and we need a fresh corporate card that represents us better. We start from cleaning carpet and tiles, to upholstery and curtains, to completely clean all contents and building materials after a fire, or completely dry out a home or business after a major or minor flood event. We are open to all concepts as we want to create a new look, maybe even logo, signage, vehicle signage, uniforms.
We are open to new colours etc.

Go to www.brightmoorcare.com.au for current logo and all other past ideas

Target Market(s)

Everyone is our possible client but we are targeting more coorporate

Industry/Entity Type

Building

```html
<!DOCTYPE html>
<html lang="en">
<head>
<meta charset="utf-8">
<title>Brightmoor Care – Business Card</title>
<link href="https://fonts.googleapis.com/css2?family=Open+Sans:wght@400;600;700&display=swap" rel="stylesheet">
<style>
  :root {
    --page-bg: #e6e6e8;
    --card-white: #ffffff;
    --brand-blue: #165a9e;
    --brand-pink: #e0187e;
    --text-light: #ffffff;
    --shadow: rgba(0, 0, 0, 0.18);
  }
  html, body {
    margin: 0;
    width: 1200px;
    height: 900px;
    overflow: hidden;
    background: var(--page-bg);
    font-family: "Open Sans", Arial, sans-serif;
  }
  .canvas {
    position: relative;
    width: 1200px;
    height: 900px;
  }
  .card {
    position: absolute;
    left: 100px;
    top: 160px;
    width: 1000px;
    height: 580px;
    background: var(--card-white);
    box-shadow: 0 18px 40px var(--shadow);
    overflow: hidden;
  }
  .card-shapes {
    position: absolute;
    inset: 0;
    width: 100%;
    height: 100%;
  }
  .shape-blue { fill: var(--brand-blue); }
  .shape-pink { fill: var(--brand-pink); }

  .brand {
    position: absolute;
    left: 40px;
    top: 220px;
    display: flex;
    align-items: center;
    gap: 14px;
  }
  .brand-dot {
    flex: none;
    width: 44px;
    height: 44px;
    border-radius: 50%;
    background: var(--brand-blue);
  }
  .brand-name {
    font-weight: 600;
    font-size: 32px;
    line-height: 1.1;
    color: var(--brand-blue);
  }
  .brand-name span { display: block; }

  .contact {
    position: absolute;
    right: 56px;
    top: 70px;
    text-align: right;
    color: var(--text-light);
  }
  .person-name {
    font-weight: 700;
    font-size: 30px;
    margin: 0;
  }
  .person-role {
    font-size: 22px;
    margin: 0 0 46px;
  }
  .address {
    font-size: 20px;
    line-height: 1.35;
    margin: 0 0 46px;
  }
  .details {
    list-style: none;
    padding: 0;
    margin: 0;
    font-size: 20px;
    line-height: 1.45;
  }
  .details li {
    display: flex;
    justify-content: flex-end;
    align-items: center;
    gap: 10px;
  }
  .details svg {
    width: 16px;
    height: 16px;
    fill: none;
    stroke: var(--text-light);
    stroke-width: 1.8;
  }
</style>
</head>
<body>
<div class="canvas">
  <div class="card">
    <svg class="card-shapes" viewBox="0 0 1000 580" preserveAspectRatio="none" aria-hidden="true">
      <path class="shape-pink" d="M490 0 L572 0 C410 110 312 330 288 580 L281 580 C298 340 360 120 490 0 Z"/>
      <path class="shape-blue" d="M605 0 C440 110 338 330 312 580 L1000 580 L1000 0 Z"/>
    </svg>

    <div class="brand">
      <span class="brand-dot"></span>
      <span class="brand-name"><span>Brightmoor</span><span>Care</span></span>
    </div>

    <div class="contact">
      <p class="person-name">Marcus Delaney</p>
      <p class="person-role">Director</p>
      <p class="address">27, 4th floor, Harbour Point<br>Road NSW</p>
      <ul class="details">
        <li>012 555 0147
          <svg viewBox="0 0 16 16"><rect x="4" y="1" width="8" height="14" rx="1.5"/></svg>
        </li>
        <li>012 555 0147
          <svg viewBox="0 0 16 16"><path d="M3 2 L6 2 L7 5 L5.5 6.5 C6.5 8.5 7.5 9.5 9.5 10.5 L11 9 L14 10 L14 13 C8 13 3 8 3 2 Z"/></svg>
        </li>
        <li>marcus@brightmoorcare.com.au
          <svg viewBox="0 0 16 16"><rect x="1.5" y="3.5" width="13" height="9"/><path d="M1.5 3.5 L8 9 L14.5 3.5"/></svg>
        </li>
        <li>www.brightmoorcare.com.au
          <svg viewBox="0 0 16 16"><circle cx="8" cy="8" r="6.5"/><path d="M1.5 8 H14.5 M8 1.5 C5 5 5 11 8 14.5 M8 1.5 C11 5 11 11 8 14.5"/></svg>
        </li>
      </ul>
    </div>
  </div>
</div>
</body>
</html>
```